Alaska Law Firm Needs a Sticker Design

We need a design for stickers to put on already-printed brochures. We mail the brochures to potential clients so they can learn more about accident-induced injuries, insurance claims, legal representation, and our own law firm.

One of our lawyers wrote a book that provides a helpful overview of personal injury claims. We are offering this book for free to anyone who calls and requests it. Therefore, the sticker design should include one of the following phrases, or something very similar:
a) "Still have questions? Call and request our book-- for free!"
b) "Still have questions about auto accident claims? Call and request our book today."
c) "Still have questions about filing a claim? Call and request a free copy of our book."
d) "Still have questions? Call us today to request a free copy of our book, Clear Lanes Ahead."
e) "To learn more about automobile accidents and insurance, call today and request a free copy of our book."

The sticker should be approximately 3"x3" and may be a circle, square, rectangle, or ellipsis. The sticker will be placed on the back of the folder, which is light blue. We would like the sticker to match the color scheme of our website and the folder.

I will upload an image of the book cover as soon as I obtain it.

Industry/Entity Type

Law Firm

Font styles to use
Serif
Sans Serif

Requirements
Should not have
• Bright colors that aren't already used in the folder design. e.g. no bright orange, pink, chartreuse, turquoise, yellow, red.

```html
<!DOCTYPE html>
<html lang="en">
<head>
<meta charset="utf-8">
<title>Still Have Questions? Sticker</title>
<link href="https://fonts.googleapis.com/css2?family=Rye&family=Lobster&family=Kurale&display=swap" rel="stylesheet">
<style>
  :root {
    --page: #f1f1f2;
    --navy: #1f2f8c;
    --navy-deep: #16226a;
    --ink: #222222;
    --paper: #ffffff;
    --paper-shade: #e4e4e6;
  }
  html, body {
    margin: 0;
    padding: 0;
    width: 1200px;
    height: 1200px;
    overflow: hidden;
    background: var(--page);
  }
  .sticker {
    display: block;
    width: 1200px;
    height: 1200px;
  }
  .headline-dark { font-family: "Rye", serif; fill: var(--ink); }
  .headline-navy { font-family: "Rye", serif; fill: var(--navy); }
  .band-script { font-family: "Lobster", cursive; fill: var(--paper); }
  .offer-line { font-family: "Kurale", serif; fill: var(--ink); }
  .outline-rule { fill: none; stroke: var(--ink); stroke-width: 3; }
  .spark { fill: var(--navy); }
</style>
</head>
<body>
<svg class="sticker" viewBox="0 0 1200 1200" xmlns="http://www.w3.org/2000/svg" aria-labelledby="sticker-title">
  <title id="sticker-title">Still have questions? Call and request our book for free!</title>
  <defs>
    <clipPath id="face-clip">
      <circle cx="600" cy="600" r="440"/>
    </clipPath>
    <linearGradient id="face-fill" x1="0" y1="0" x2="0" y2="1">
      <stop offset="0" stop-color="var(--paper-shade)"/>
      <stop offset="0.45" stop-color="var(--paper)"/>
      <stop offset="1" stop-color="var(--paper)"/>
    </linearGradient>
    <linearGradient id="band-fill" x1="0" y1="0" x2="1" y2="0">
      <stop offset="0" stop-color="var(--navy-deep)"/>
      <stop offset="0.5" stop-color="var(--navy)"/>
      <stop offset="1" stop-color="var(--navy-deep)"/>
    </linearGradient>
    <polygon id="spark-shape" points="0,-23 4,-10 16,-16 10,-4 23,0 10,4 16,16 4,10 0,23 -4,10 -16,16 -10,4 -23,0 -10,-4 -16,-16 -4,-10"/>
  </defs>

  <!-- sticker body -->
  <circle class="sticker-rim" cx="600" cy="600" r="458" fill="var(--navy)"/>
  <circle class="sticker-face" cx="600" cy="600" r="440" fill="url(#face-fill)"/>

  <!-- middle band -->
  <rect class="sticker-band" x="140" y="528" width="920" height="201" fill="url(#band-fill)" clip-path="url(#face-clip)"/>

  <!-- inner outline segments -->
  <path class="outline-rule" d="M189 514 A420 420 0 0 1 1011 514 Z"/>
  <path class="outline-rule" d="M205 743 L995 743 A420 420 0 0 1 205 743 Z"/>

  <!-- headline -->
  <text class="headline-dark" x="586" y="349" text-anchor="middle" font-size="132" textLength="332" lengthAdjust="spacingAndGlyphs">STILL</text>
  <use class="spark" href="#spark-shape" x="312" y="409"/>
  <use class="spark" href="#spark-shape" x="851" y="409"/>
  <text class="headline-navy" x="586" y="480" text-anchor="middle" font-size="132" textLength="358" lengthAdjust="spacingAndGlyphs">HAVE</text>

  <!-- band script -->
  <text class="band-script" x="611" y="672" text-anchor="middle" font-size="165" textLength="733" lengthAdjust="spacingAndGlyphs">Questions?</text>

  <!-- offer -->
  <text class="offer-line" x="590" y="815" text-anchor="middle" font-size="52" textLength="563" lengthAdjust="spacingAndGlyphs">Call and request our book</text>
  <text class="headline-navy" x="591" y="916" text-anchor="middle" font-size="84" textLength="458" lengthAdjust="spacingAndGlyphs">FOR FREE!</text>
</svg>
</body>
</html>
```